Progressive Metal Band Looking for Unique New Album Cover

We are a progressive/thrash metal band called Velvet Hollow and are looking for a thought provoking design for our upcoming album "A spark to Transcend" which when broken down means to us "A tick" is a moment in the past that feels like it's moved by very fast and "Ameliorate" to improve or make something better.

This album is a collection of some of our older songs that haven't been released yet so the theme that we want this cover to represent is progression itself (our personal progression). Though we are a metal band and like to use some graphic imagery we like to try and distance ourselves from the typical demons and skulls. The style of the design that we're looking for would be something painted or hand drawn, something that looks natural or at least not so computer generated. An idea for how we want the album to be presented we were thinking one way that we could have a visual representation of progression would be a clarity gradient from left to right. Have the detail of the design become more sharp and detailed but we are open to changes as well as letting creative liberties being taken in order to allow the best possible product to be made.

We want this design to cover the front and back of the package so the design in mind would need to fill a 5x10 digipak. I've also attached demo's of two songs that will appear on this album as well as some imagery that we've associated ourselves with in the past. We do have a logo that due to its size could not be uploaded here, once the final design is chosen we would like to have it added to the design (the logo in the images provided is the logo that will be used).

The track list for the album is:
1. Grimwake
2. Mechanized Bondage
3. Storm of Spite
4. Rivers of Dust
5. Pancake Outlaw

Target Market(s)

Metal, Progressive Metal, Thrash Metal, Hard Rock

Industry/Entity Type

Progressive

Requirements
Should not have
• Clocks, hourglasses, bugs, cocoons

```html
<!DOCTYPE html>
<html lang="en">
<head>
<meta charset="UTF-8">
<title>Album Back Cover – Tracklist</title>
<link href="https://fonts.googleapis.com/css2?family=Oswald:wght@600&display=swap" rel="stylesheet">
<style>
  :root {
    --ink-deep: #161d22;
    --ink-mid: #1a2227;
    --ink-edge: #1d262b;
    --speck-tan: #b9a283;
    --type-white: #f5f3ee;
  }
  html, body {
    margin: 0;
    padding: 0;
    width: 1200px;
    height: 1200px;
    overflow: hidden;
    background: var(--ink-deep);
  }
  .back-cover {
    position: relative;
    width: 1200px;
    height: 1200px;
    overflow: hidden;
  }
  .back-cover__texture {
    position: absolute;
    inset: 0;
    width: 100%;
    height: 100%;
  }
  .tracklist {
    position: absolute;
    left: 0;
    right: 0;
    top: 442px;
    margin: 0;
    padding: 0;
    list-style: none;
    text-align: center;
    font-family: "Oswald", "Arial Narrow", sans-serif;
    font-weight: 600;
    font-variant: small-caps;
    font-size: 50px;
    line-height: 64px;
    letter-spacing: 0.5px;
    color: var(--type-white);
    white-space: nowrap;
  }
  .tracklist__item {
    margin: 0;
  }
</style>
</head>
<body>
  <main class="back-cover">
    <svg class="back-cover__texture" viewBox="0 0 1200 1200" role="img"
         aria-label="Dark worn grunge texture with scattered tan paint speckles, heaviest at the top left and bottom right corners">
      <defs>
        <radialGradient id="speckle-top-left" cx="0.1" cy="0.15" r="0.45">
          <stop offset="0" stop-color="var(--speck-tan)" stop-opacity="0.12"/>
          <stop offset="1" stop-color="var(--speck-tan)" stop-opacity="0"/>
        </radialGradient>
        <radialGradient id="speckle-bottom-right" cx="0.95" cy="0.92" r="0.35">
          <stop offset="0" stop-color="var(--speck-tan)" stop-opacity="0.14"/>
          <stop offset="1" stop-color="var(--speck-tan)" stop-opacity="0"/>
        </radialGradient>
        <linearGradient id="base-wash" x1="0" y1="0" x2="1" y2="1">
          <stop offset="0" stop-color="var(--ink-mid)"/>
          <stop offset="0.5" stop-color="var(--ink-deep)"/>
          <stop offset="1" stop-color="var(--ink-edge)"/>
        </linearGradient>
      </defs>
      <rect width="1200" height="1200" fill="url(#base-wash)"/>
      <rect width="1200" height="1200" fill="url(#speckle-top-left)"/>
      <rect width="1200" height="1200" fill="url(#speckle-bottom-right)"/>
    </svg>

    <ol class="tracklist" aria-label="Tracklist">
      <li class="tracklist__item">1. Grimwake</li>
      <li class="tracklist__item">2. Mechanized Bondage</li>
      <li class="tracklist__item">3. Storm of Spite</li>
      <li class="tracklist__item">4. Rivers of Dust</li>
      <li class="tracklist__item">5. Pancake Outlaw</li>
    </ol>
  </main>
</body>
</html>
```